buisnes card for Willowmere Reflexology

I need a new business card with my information
Hedwig Branstoe
MCSRI,RCRT,RN(Grermany)
Cranio-Sacral Reflexology
Facial Reflexology, Kallodrevmetode TM
Nerve point Reflexology
41627 Marrowfield Road
Abbotsford,BC
Willowmerereflexology.ca
I would like the design to show that I work mostly with clients that have health problems.(80% are back/spine related problems).
I would like the card to be professional as well as inviting. I like nature aspects as well.
I have two websites that I like so you have an Idea what kind of design speaks to me.
1. www.tendravo.ca the craft of mending (Chilliwack)
2.www.quietharbourdoulacare.ca (Abbotsford)

My treatment room is blue and the outside of our house is dark blue and grey. That are colors that could be incorporated

clients that are looking for a more natural approach to their health issues

Health And Wellness

Hedwig Branstoe
MCSRI,RCRT,RN(Grermany)
Cranio-Sacral Reflexology
Nerve point Reflexology
41627 Marrowfield Road
Abbotsford,BC
Willowmerereflexology.ca

0355a3
0492cd

• name, address, phonenumber
• 1. www.tendravo.ca the craft of mending (Chilliwack)
• 2.www.quietharbourdoulacare.ca (Abbotsford)
• This are designs that I like.

```html
<!DOCTYPE html>
<html lang="en">
<head>
<meta charset="utf-8">
<title>Willowmere Reflexology – Business Card</title>
<link rel="stylesheet" href="https://fonts.googleapis.com/css2?family=Lato:wght@300;400;700&family=Arimo:wght@400;700&display=swap">
<style>
  :root {
    --stage: #e9eaec;
    --card: #ffffff;
    --navy: #063a6a;
    --brand-blue: #0355a3;
    --bright-blue: #0492cd;
    --ink: #222629;
    --soft-ink: #333;
  }
  * { margin: 0; padding: 0; box-sizing: border-box; }
  html, body { width: 1200px; height: 688px; overflow: hidden; }
  body { background: var(--stage); position: relative; font-family: "Lato", sans-serif; color: var(--ink); }

  .card {
    position: absolute; top: 175px; width: 547px; height: 337px;
    background: var(--card); overflow: hidden;
    box-shadow: 0 2px 6px rgba(0,0,0,.18);
  }
  .card--front { left: 35px; }
  .card--back { left: 618px; font-family: "Arimo", sans-serif; }

  .front-sweep { position: absolute; inset: 0; }

  .brand { position: absolute; left: 26px; top: 44px; display: flex; align-items: center; gap: 8px;
    font-size: 23px; font-weight: 400; color: var(--brand-blue); letter-spacing: .3px; }
  .brand__dot { width: 12px; height: 12px; border-radius: 50%; background: var(--brand-blue); }

  .services { position: absolute; right: 117px; top: 106px; list-style: none; text-align: right;
    font-size: 12.5px; line-height: 17.5px; color: var(--ink); }
  .services li::after { content: "\2022"; margin-left: 5px; color: var(--navy); }
  .services li.services__tm::after { content: ""; margin-left: 0; margin-right: 10px; }

  .person { position: absolute; left: 33px; top: 173px; }
  .person__name { font-size: 20px; font-weight: 400; color: var(--ink); letter-spacing: .2px; }
  .person__creds { font-size: 12px; color: var(--brand-blue); margin-top: 2px; }

  .contact { position: absolute; left: 33px; top: 232px; list-style: none; font-size: 12.5px; line-height: 20px; }
  .contact li { display: flex; align-items: flex-start; gap: 9px; }
  .contact svg { width: 11px; height: 11px; margin-top: 4px; flex: none; fill: var(--brand-blue); }
  .contact__address { line-height: 18px; margin-top: 1px; }

  .appointments__title { position: absolute; top: 56px; left: 0; right: 0; text-align: center;
    font-size: 16px; font-weight: 700; color: var(--navy); letter-spacing: .2px; }
  .appointments__rows { position: absolute; left: 139px; top: 103px; list-style: none; font-size: 14px; color: var(--soft-ink); }
  .appointments__rows li { display: flex; align-items: flex-end; height: 37px; }
  .blank { display: inline-block; border-bottom: 1px solid #555; height: 16px; }
  .blank--date { width: 123px; }
  .blank--time { width: 85px; }
  .word-at { margin: 0 8px; }
  .word-ampm { margin-left: 7px; }
  .appointments__note { position: absolute; top: 263px; left: 0; right: 0; text-align: center;
    font-size: 13px; color: var(--soft-ink); }
</style>
</head>
<body>

<section class="card card--front" aria-label="Business card front">
  <svg class="front-sweep" viewBox="0 0 547 337" width="547" height="337" aria-hidden="true">
    <path d="M412 0 C515 70 470 250 188 337 L547 337 L547 0 Z" fill="var(--brand-blue)"/>
    <path d="M420 0 C522 70 478 252 205 337 L547 337 L547 0 Z" fill="#ffffff"/>
    <path d="M428 0 C532 72 488 256 226 337 L547 337 L547 0 Z" fill="var(--navy)"/>
  </svg>

  <div class="brand"><span class="brand__dot"></span>Willowmere Reflexology</div>

  <ul class="services">
    <li>Cranio-Sacral Reflexology</li>
    <li>Facial Reflexology</li>
    <li class="services__tm">Kallodrevmetode TM</li>
    <li>Nerve point Reflexology</li>
  </ul>

  <div class="person">
    <p class="person__name">Hedwig Branstoe</p>
    <p class="person__creds">MCSRI,RCRT,RN(Grermany)</p>
  </div>

  <ul class="contact">
    <li>
      <svg viewBox="0 0 24 24"><path d="M6.6 10.8a15.1 15.1 0 0 0 6.6 6.6l2.2-2.2c.3-.3.7-.4 1-.2 1.1.4 2.3.6 3.6.6.6 0 1 .4 1 1V20c0 .6-.4 1-1 1A17 17 0 0 1 3 4c0-.6.4-1 1-1h3.5c.6 0 1 .4 1 1 0 1.3.2 2.5.6 3.6.1.3 0 .7-.2 1z"/></svg>
      <span>604 555-0182</span>
    </li>
    <li>
      <svg viewBox="0 0 24 24"><path d="M12 2a10 10 0 1 0 0 20 10 10 0 0 0 0-20zm6.9 6h-3a15.6 15.6 0 0 0-1.3-3.9A8 8 0 0 1 18.9 8zM12 4c.8 1.2 1.5 2.5 1.9 4h-3.8c.4-1.5 1.1-2.8 1.9-4zM4.3 14a8 8 0 0 1 0-4h3.4a16 16 0 0 0 0 4zm.8 2h3a15.6 15.6 0 0 0 1.3 3.9A8 8 0 0 1 5.1 16zm3-8h-3a8 8 0 0 1 4.3-3.9C8.8 5.3 8.4 6.6 8.1 8zM12 20c-.8-1.2-1.5-2.5-1.9-4h3.8c-.4 1.5-1.1 2.8-1.9 4zm2.3-6H9.7a14.7 14.7 0 0 1 0-4h4.6a14.7 14.7 0 0 1 0 4zm.3 5.9c.6-1.1 1-2.4 1.3-3.9h3a8 8 0 0 1-4.3 3.9zm1.7-5.9a16 16 0 0 0 0-4h3.4a8 8 0 0 1 0 4z"/></svg>
      <span>willowmerereflexology.ca</span>
    </li>
    <li>
      <svg viewBox="0 0 24 24"><path d="M12 2a7 7 0 0 0-7 7c0 5.2 7 13 7 13s7-7.8 7-13a7 7 0 0 0-7-7zm0 9.5A2.5 2.5 0 1 1 12 6.5a2.5 2.5 0 0 1 0 5z"/></svg>
      <span class="contact__address">41627 Marrowfield Road<br>Abbotsford, BC</span>
    </li>
  </ul>
</section>

<section class="card card--back" aria-label="Business card back">
  <h2 class="appointments__title">Your Next Scheduled Appointments:</h2>
  <ul class="appointments__rows">
    <li><span class="blank blank--date"></span><span class="word-at">at</span><span class="blank blank--time"></span><span class="word-ampm">am/pm</span></li>
    <li><span class="blank blank--date"></span><span class="word-at">at</span><span class="blank blank--time"></span><span class="word-ampm">am/pm</span></li>
    <li><span class="blank blank--date"></span><span class="word-at">at</span><span class="blank blank--time"></span><span class="word-ampm">am/pm</span></li>
    <li><span class="blank blank--date"></span><span class="word-at">at</span><span class="blank blank--time"></span><span class="word-ampm">am/pm</span></li>
  </ul>
  <p class="appointments__note">(24 hours notice is required for cancellations)</p>
</section>

</body>
</html>
```